Upscale business cards needed for Board of Directors

We need professional business cards created for members of our family business Board of Directors. We would like these relatively simple and straightforward, but also with a unique element to set them apart. Probably stick with neutral and simple colors - white, grey etc. We need space for the traditional elements, including name, title, address, email/phone number. And we will be creating several from this template so it needs to be template that is easy to switch information in and out of.
Business
See description

```html
<!DOCTYPE html>
<html lang="en">
<head>
<meta charset="utf-8">
<title>Harborline Holdings – Business Card</title>
<link href="https://fonts.googleapis.com/css2?family=Source+Sans+3:wght@400;600;700&display=swap" rel="stylesheet">
<style>
  :root {
    --page-bg: #e6e6e6;
    --card-dark: #333233;
    --card-light: #ffffff;
    --ink: #1e1c1d;
    --name-on-dark: #6a696a;
    --muted: #7d7d7d;
    --url-dark: #8f8f8f;
    --gold: #b49a6d;
  }
  * { box-sizing: border-box; margin: 0; padding: 0; }
  html, body {
    width: 1200px; height: 1000px; overflow: hidden;
    background: var(--page-bg);
    font-family: "Source Sans 3", "Myriad Pro", Arial, sans-serif;
  }
  .canvas { position: relative; width: 1200px; height: 1000px; }
  .card {
    position: absolute; left: 287px; width: 626px; height: 357px;
    box-shadow: 0 3px 10px rgba(0,0,0,0.18);
  }
  .card--front { top: 140px; background: var(--card-dark); }
  .card--back { top: 532px; background: var(--card-light); }

  .company-name { font-weight: 600; line-height: 1; white-space: nowrap; }
  .card--front .company-name {
    position: absolute; left: 0; right: 0; top: 154px;
    text-align: center; font-size: 44px; color: var(--name-on-dark);
  }
  .front-url {
    position: absolute; left: 0; right: 0; top: 308px;
    text-align: center; font-size: 14px; color: var(--url-dark);
  }

  .card--back .company-name {
    position: absolute; left: 28px; top: 166px; width: 272px;
    text-align: center; font-size: 25px; color: var(--ink);
  }

  .divider {
    position: absolute; left: 312px; top: 107px; width: 1px; height: 144px;
    background: var(--gold);
  }
  .contact { position: absolute; left: 338px; top: 104px; color: var(--muted); font-size: 14px; }
  .contact__name { color: var(--gold); font-size: 18px; font-weight: 600; line-height: 22px; }
  .contact__title { font-size: 14px; line-height: 18px; margin-bottom: 12px; }
  .contact__list { list-style: none; }
  .contact__item { display: flex; align-items: center; gap: 6px; line-height: 18px; }
  .contact__item svg { width: 11px; height: 11px; flex: none; }
  .contact__address { margin-top: 8px; line-height: 18px; }
</style>
</head>
<body>
<main class="canvas">
  <section class="card card--front">
    <p class="company-name">Harborline Holdings</p>
    <p class="front-url">www.harborlineholdings.com</p>
  </section>

  <section class="card card--back">
    <p class="company-name">Harborline Holdings</p>
    <div class="divider"></div>
    <div class="contact">
      <p class="contact__name">Daniel Reeves</p>
      <p class="contact__title">President</p>
      <ul class="contact__list">
        <li class="contact__item">
          <svg viewBox="0 0 12 12" aria-hidden="true"><rect x="3" y="0.5" width="6" height="11" rx="1" fill="none" stroke="#b49a6d" stroke-width="1.2"/><rect x="5" y="9" width="2" height="1" fill="#b49a6d"/></svg>
          010-555-0142
        </li>
        <li class="contact__item">
          <svg viewBox="0 0 12 12" aria-hidden="true"><rect x="0.5" y="2.5" width="11" height="7" fill="#b49a6d"/><path d="M0.5 2.5 L6 7 L11.5 2.5" fill="none" stroke="#fff" stroke-width="1"/></svg>
          info@harborlineholdings.com
        </li>
        <li class="contact__item">
          <svg viewBox="0 0 12 12" aria-hidden="true"><circle cx="6" cy="6" r="5" fill="#b49a6d"/><path d="M1 6 H11 M6 1 C3.5 3.5 3.5 8.5 6 11 M6 1 C8.5 3.5 8.5 8.5 6 11" fill="none" stroke="#fff" stroke-width="0.7"/></svg>
          www.harborlineholdings.com
        </li>
      </ul>
      <p class="contact__address">Street name, Suite 100 State,<br>Zip Code, Country</p>
    </div>
  </section>
</main>
</body>
</html>
```